Tall Harbor Business Card

We are a Video Production and Video Equipment Rental company specialising in the supply of state of the art Video Technology and Services for the Live Entertainment, Television and Corporate Business Theatre markets. (in Sydney, Australia) www.tallharbor.example

Industry/Entity Type

Business

Contact Information for Business Card

name, position, email, website, address, logo
Example attached of the information we need - doesn't necessarily have to look the same

Font styles to use
Other font styles liked:
• Tall Harbor logo font is GOTHAM

Colors
ea1f27

Requirements
Nice to have
• either matt black or shiny black cards -
raised logo

```html
<!DOCTYPE html>
<html lang="en">
<head>
<meta charset="utf-8">
<title>Tall Harbor Business Card</title>
<link href="https://fonts.googleapis.com/css2?family=Montserrat:wght@500&family=Open+Sans:wght@400;600;700&display=swap" rel="stylesheet">
<style>
  :root {
    --red: #ea1f27;
    --charcoal: #333335;
    --slate: #4b4b4e;
    --graphite: #39393b;
    --white: #ffffff;
    --ink: #333333;
    --muted: #666666;
    --backdrop: #e9e9ea;
  }
  html, body {
    margin: 0;
    width: 1200px;
    height: 960px;
    overflow: hidden;
    background: var(--backdrop);
    font-family: "Open Sans", Arial, sans-serif;
  }
  .canvas {
    position: relative;
    width: 1200px;
    height: 960px;
  }
  .card {
    position: absolute;
    top: 130px;
    width: 400px;
    height: 700px;
    overflow: hidden;
    box-shadow: 0 10px 30px rgba(0,0,0,0.18);
  }
  .card--front { left: 150px; background: var(--charcoal); }
  .card--back { left: 650px; background: var(--white); }

  .wordmark {
    display: flex;
    align-items: center;
    gap: 12px;
    font-family: "Montserrat", "Helvetica Neue", sans-serif;
    font-weight: 500;
    color: var(--white);
    letter-spacing: 1px;
    white-space: nowrap;
  }
  .wordmark__mark {
    width: 14px;
    height: 14px;
    background: var(--red);
  }
  .card--front .wordmark {
    position: absolute;
    left: 0; right: 0;
    top: 255px;
    justify-content: center;
    font-size: 40px;
  }
  .tagline {
    position: absolute;
    left: 0; right: 0;
    top: 560px;
    height: 90px;
    background: var(--white);
    display: flex;
    flex-direction: column;
    justify-content: center;
    align-items: center;
    font-size: 17px;
    line-height: 26px;
    color: var(--ink);
  }
  .front-foot {
    position: absolute;
    left: 0; right: 0; bottom: 0;
    height: 50px;
    background: var(--red);
  }

  .back-top { height: 45px; background: var(--red); }
  .identity {
    height: 315px;
    display: flex;
    flex-direction: column;
    justify-content: center;
    padding-left: 60px;
  }
  .identity__name {
    margin: 0;
    font-size: 40px;
    font-weight: 400;
    color: var(--muted);
    line-height: 1.1;
  }
  .identity__name strong { font-weight: 700; color: var(--ink); }
  .identity__role {
    margin: 4px 0 0;
    font-size: 21px;
    letter-spacing: 0.5px;
    color: var(--muted);
  }
  .brand-band {
    height: 110px;
    background: var(--charcoal);
    display: flex;
    align-items: center;
    justify-content: center;
  }
  .brand-band .wordmark { font-size: 38px; }
  .contact-row {
    height: 90px;
    display: flex;
    align-items: center;
    gap: 26px;
    padding-left: 60px;
    color: var(--white);
    font-size: 14px;
    line-height: 22px;
    letter-spacing: 0.4px;
  }
  .contact-row--address { background: var(--slate); }
  .contact-row--web { background: var(--graphite); }
  .contact-row svg { flex: none; }
  .back-foot {
    border-top: 6px solid var(--white);
    height: 34px;
    background: var(--red);
    border-bottom: 10px solid var(--white);
  }
</style>
</head>
<body>
<main class="canvas">
  <section class="card card--front" aria-label="Card front">
    <div class="wordmark"><span class="wordmark__mark"></span>TALL HARBOR</div>
    <div class="tagline">
      <span>Video Solutions - LED Screens</span>
      <span>Camera Systems - Projection</span>
    </div>
    <div class="front-foot"></div>
  </section>

  <section class="card card--back" aria-label="Card back">
    <div class="back-top"></div>
    <div class="identity">
      <h1 class="identity__name"><strong>Sam</strong> Ferretti</h1>
      <p class="identity__role">MANAGING DIRECTOR</p>
    </div>
    <div class="brand-band">
      <div class="wordmark"><span class="wordmark__mark"></span>TALL HARBOR</div>
    </div>
    <div class="contact-row contact-row--address">
      <svg width="26" height="34" viewBox="0 0 26 34" aria-hidden="true">
        <path d="M13 1C6.4 1 1 6.3 1 12.8 1 21.5 13 33 13 33s12-11.5 12-20.2C25 6.3 19.6 1 13 1z" fill="#9a9a9d"/>
        <circle cx="13" cy="12.5" r="4.5" fill="#4b4b4e"/>
      </svg>
      <span>12 Quay Lane Marrick<br>NSW 2000 Australia</span>
    </div>
    <div class="contact-row contact-row--web">
      <svg width="32" height="32" viewBox="0 0 32 32" aria-hidden="true" fill="none" stroke="#9a9a9d" stroke-width="2">
        <circle cx="16" cy="16" r="14"/>
        <ellipse cx="16" cy="16" rx="6" ry="14"/>
        <line x1="2" y1="16" x2="30" y2="16"/>
        <path d="M5 9h22M5 23h22"/>
      </svg>
      <span>SAM@TALLHARBOR.EXAMPLE<br>WWW.TALLHARBOR.EXAMPLE</span>
    </div>
    <div class="back-foot"></div>
  </section>
</main>
</body>
</html>
```